Book Cover (QUIET WEEKS MEND EVERY KNOT)

This book is a series of blog posts from my blog, Sparks Kept Handy, which is at glenferrante.example/blog.
The book is to be called:
QUIET WEEKS MEND EVERY KNOT
And 51 other Sparks Kept Handy from the Corner Shop Tutor
(Sparks Kept Handy) should be italicized.
My name is Glen Ferrante, M.B.A.

I will need three variations for my paperback, hardcover and e-book.
Here are some of the blog titles and their topics:
Preparing Your Small Business For Recession small business recession
Should I Incorporate My Business? Should I Incorporate My Business?
Alternative to Minority Shareholder In Small Private Companies minority shareholder
Small Business Culture – Getting it Right Small Business Culture
What is The Right Way to Fire Someone The Right Way to Fire Someone
The Five Basic Leadership Principles Leadership Principles
10 Tips for New Entrepreneurs – Sure Ways to Increase Your Chances of Success
10 things to consider before becoming an entrepreneur
Strategy vs Biz Plans small business strategy
Closing Sales close the sale
Breakeven break even
Growth makes cash flow suck cash flow issues
Think Twice About Offering Early Payment Discounts prepayment discounts
Firing Customers firing customers
Collections best practices getting paid faster
The Cash Flow Statement cash flow statement
Using Paralegals paralegal
Radical Candor radical candor
Why No is the Second Best Word to a Salesperson's ears value of no
The $8 Million Problem -
Contractor vs Employee contractor vs employee
The Columbo sales tactic
Systems Turn Goals From Dreams Into Reality Systems vs Goals
The Importance of Realistic Goals stretch goals
Why The Owner Must Review Every Hire hiring for values
Systems Thinking for Small Biz: The Case for SOPs systems thinking
Trust Your Gut business intuition
Grease and friction grease vs friction
Left alone, 90% of problems solve themselves strategic inaction
Referrals Are Great—But Not a Growth Strategy referrals
The Lean Marketing Machine: 7 Hacks to Grow Your Small Business Fast marketing hacks
The Small Business Health Check small business health check
How to Spot a Customer Headed for Trouble — Before They Take You Down With Them customer warning signs
We Are What We Repeatedly Do habits
The Smartest People Know When to Play Dumb playing dumb
Before You Scale, Do the Math unit economics
AI for Small Business: Practical Tools and Use Cases AI for Small Business
Title: Tell Me Right Now—Why Can’t We Raise Your Prices? small business pricing
Why Your Real Competitor Isn’t Who You Think creative destruction
Good Enough Might Be Great satisficing
Bootstrapping: Building Your Business on Your Terms bootstrapping
Building Resilient Companies That Never Have to Bet the Farm bet the farm
We Always Overshoot: From Fiber to Cannabis to AI AI overbuild
A Bias Toward Action bias toward ation
Choosing the Right Business Owner Title business owner title
Jobs to Be Done: Understanding What Your Customers Really Want Jobs to Be Done
Forget Money. Here’s What Really Motivates People. motivation

Target Market(s)

Small business operators, business school students

Industry/Entity Type

Small business

Colors

Designer to choose colors to be used in the design.

Requirements
Should not have
• Should not look cartoonish

```html
<!DOCTYPE html>
<html lang="en">
<head>
<meta charset="utf-8">
<title>Quiet Weeks Mend Every Knot — Book Cover</title>
<link rel="stylesheet" href="https://fonts.googleapis.com/css2?family=Nunito:wght@800;900&family=Source+Serif+4:ital,opsz,wght@1,8..60,400&display=swap">
<style>
  :root {
    --cover-navy: #13304f;
    --title-white: #ffffff;
    --art-tone-light: #3b5470;
    --art-tone-dark: #1a3757;
  }
  html, body {
    margin: 0;
    padding: 0;
    overflow: hidden;
    background: var(--cover-navy);
  }
  .cover {
    position: relative;
    width: 1200px;
    height: 900px;
    background: var(--cover-navy);
    overflow: hidden;
  }
  .cover-title {
    position: absolute;
    left: 219px;
    top: 14px;
    margin: 0;
    font-family: "Nunito", sans-serif;
    font-weight: 900;
    font-size: 136px;
    line-height: 111px;
    letter-spacing: 0;
    color: var(--title-white);
    text-transform: uppercase;
    white-space: nowrap;
  }
  .cover-title span { display: block; }
  .cover-subtitle {
    position: absolute;
    left: 227px;
    top: 503px;
    margin: 0;
    font-family: "Source Serif 4", serif;
    font-style: italic;
    font-weight: 400;
    color: var(--title-white);
    white-space: nowrap;
  }
  .cover-subtitle span { display: block; }
  .subtitle-lead { font-size: 37px; line-height: 52px; }
  .subtitle-tail { font-size: 29px; line-height: 40px; }
  .growth-artwork {
    position: absolute;
    left: 109px;
    top: 500px;
    width: 926px;
    height: 325px;
    background: linear-gradient(135deg, var(--art-tone-dark) 0%, var(--art-tone-light) 100%);
    clip-path: polygon(53% 0, 100% 0, 100% 100%, 0 100%, 0 45%, 53% 45%);
    opacity: 0.7;
  }
  .cover-author {
    position: absolute;
    left: 0;
    width: 1200px;
    top: 853px;
    margin: 0;
    text-align: center;
    font-family: "Nunito", sans-serif;
    font-weight: 800;
    font-size: 24px;
    letter-spacing: 0.5px;
    color: var(--title-white);
  }
</style>
</head>
<body>
<main class="cover">
  <h1 class="cover-title">
    <span>Quiet</span>
    <span>Weeks</span>
    <span>Mend Every</span>
    <span>Knot</span>
  </h1>

  <p class="cover-subtitle">
    <span class="subtitle-lead">and 51 other <em>sparks</em></span>
    <span class="subtitle-lead"><em>kept handy</em> from</span>
    <span class="subtitle-tail">the corner shop tutor</span>
  </p>

  <div class="growth-artwork" role="img" aria-label="Abstract grey line diagram of circles and nodes connected along a baseline, rising into an upward arrow"></div>

  <p class="cover-author">GLEN FERRANTE, M.B.A.</p>
</main>
</body>
</html>
```